New Letterhead

Improve the attached letterhead to make it more alive and corporate class using the company colors in the two companies logos available on the two companies website.

Industry/Entity Type

Construction Company

Requirements
Must have
• colours of the two logod
Nice to have
• Be more alive and professional
Should not have
• Any other colours besides the ones in the logos

```html
<!DOCTYPE html>
<html lang="en">
<head>
<meta charset="utf-8">
<title>Brightvale Letterhead</title>
<link rel="stylesheet" href="https://fonts.googleapis.com/css2?family=Mulish:wght@400;700;800&family=Open+Sans:wght@400;700&display=swap">
<style>
  :root {
    --brand-red: #9b1b1e;
    --brand-dark: #1f2328;
    --text-grey: #4a4d52;
    --muted-grey: #7b7e83;
    --divider-grey: #cfd1d4;
    --paper: #ffffff;
    --backdrop: #ecedef;
  }
  * { margin: 0; padding: 0; box-sizing: border-box; }
  html, body { width: 1200px; height: 800px; overflow: hidden; }
  body {
    background: var(--backdrop);
    font-family: "Mulish", "Open Sans", sans-serif;
    color: var(--text-grey);
  }
  .letterhead {
    position: absolute;
    left: 330px; top: 18px;
    width: 540px; height: 764px;
    background: var(--paper);
    box-shadow: 0 2px 10px rgba(0,0,0,.08);
  }
  .top-rule { position: absolute; left: 0; right: 0; top: 36px; height: 8px; }
  .tagline {
    position: absolute; right: 38px; top: 10px;
    text-align: right; font-size: 6.5px; line-height: 1.25;
    letter-spacing: .08em; text-transform: uppercase; color: var(--muted-grey);
    font-weight: 700;
  }
  .tagline .accent { color: var(--brand-red); }
  .brand {
    position: absolute; left: 46px; top: 70px;
    display: flex; align-items: center; gap: 8px;
  }
  .brand-name {
    font-family: "Mulish", sans-serif; font-weight: 800; font-size: 26px;
    color: var(--brand-dark); letter-spacing: .01em;
  }
  .brand-square { width: 12px; height: 12px; background: var(--brand-red); }
  .letter-body {
    position: absolute; left: 92px; right: 46px; top: 150px;
    font-size: 10.5px; line-height: 1.5; text-align: justify;
  }
  .letter-body p { margin-bottom: 10px; }
  .closing { position: absolute; left: 92px; top: 520px; font-size: 10.5px; line-height: 1.6; }
  .footer { position: absolute; left: 46px; right: 38px; top: 612px; height: 100px; }
  .footer-rule { position: absolute; left: 0; right: 0; top: 0; height: 1px; background: var(--brand-red); }
  .footer-block {
    position: absolute; top: 12px; font-family: "Open Sans", sans-serif;
    font-size: 8px; line-height: 1.35; color: var(--muted-grey);
  }
  .footer-block strong { color: var(--brand-dark); }
  .address-primary { left: 0; width: 160px; }
  .address-partner { left: 168px; width: 130px; padding-left: 12px; border-left: 1px solid var(--divider-grey); }
  .registration { right: 0; width: 160px; text-align: right; }
  .registration .directors-title { margin-top: 6px; color: var(--brand-dark); font-weight: 700; }
  .bottom-rule { position: absolute; left: 0; right: 0; bottom: 22px; height: 8px; }
</style>
</head>
<body>
  <main class="letterhead">
    <svg class="top-rule" viewBox="0 0 540 8" preserveAspectRatio="none" aria-hidden="true">
      <rect x="0" y="2" width="500" height="3" fill="var(--brand-red)"/>
      <polygon points="492,2 512,2 506,5 488,5" fill="var(--brand-dark)"/>
    </svg>

    <div class="tagline">Building lasting value<br>on every site,<br>with care, <span class="accent">each day</span></div>

    <div class="brand">
      <span class="brand-name">Brightvale</span>
      <span class="brand-square"></span>
    </div>

    <section class="letter-body">
      <p>Dear :</p>
      <p>Lorem ipsum dolor sit amet, consectetur adipiscing elit. Aenean ut ipsum eget massa hendrerit vestibulum vel in velit. Donec pretium neque velit.</p>
      <p>Aliquam porta lectus nec mauris ornare venenatis. Vivamus non est turpis, et cursus sem. Mauris vehicula erat in diam auctor at bibendum nisl lacinia.</p>
      <p>Morbi imperdiet neque vehicula nunc convallis gravida. Vestibulum iaculis pretium placerat. Integer consequat, est sit amet facilisis eleifend, nibh nibh varius orci, eget dapibus arcu dui non purus. Pellentesque in magna mauris. Duis enim sapien, dictum vitae condimentum a, pulvinar vel lacus. Mauris et molestie nibh. Vestibulum vitae at metus elementum porta sit amet interdum elit. Nulla sollicitudin nulla volutpat congue.</p>
      <p>Suspendisse sit id dapibus fermentum, turpis sapien ornare dui, ac congue purus. Nunc sed ante dui, in porta lectus. Cras nec habitasse platea dictumst. Maecenas id diam quis dui porta felis. Donec ullamcorper mattis posuere. Phasellus vel dapibus. Vestibulum ante ipsum.</p>
      <p>Sed dapibus fermentum, turpis sapien ornare dui, ac congue purus. Nunc sed ante dui, in porta lectus. Cras nec platea dictumst. Maecenas id diam quis dui porta ullamcorper mattis posuere. Phasellus vestibulum ante ipsum.</p>
    </section>

    <div class="closing">Yours sincerely,<br><br>Signed</div>

    <footer class="footer">
      <div class="footer-rule"></div>
      <div class="footer-block address-primary">
        Brightvale JV (Pty) Limited<br>
        12 Oak Lane Rosebank,<br>
        Johannesburg<br>
        PO Box 51020, Parkview, 2122<br>
        South Africa<br>
        <strong>T: +27 (0)11 555 0142</strong><br>
        <strong>www.brightvale.example</strong>
      </div>
      <div class="footer-block address-partner">
        Brightvale Partners (Pty) Limited<br>
        7 Cedar Street, Cnr Main<br>
        Avenue Hillcrest,<br>
        Johannesburg 2001<br>
        South Africa<br>
        <strong>T: +27 (0)11 555 0187</strong><br>
        <strong>www.stonebridge.example</strong>
      </div>
      <div class="footer-block registration">
        Registration No. 2019/104572/07<br>
        Trading as Brightvale Partners (Pty) Limited
        <div class="directors-title">Directors:</div>
        <strong>Martin Keller</strong><br>
        <strong>Thabo Ndlovu</strong>
      </div>
    </footer>

    <svg class="bottom-rule" viewBox="0 0 540 8" preserveAspectRatio="none" aria-hidden="true">
      <rect x="0" y="0" width="540" height="2.5" fill="var(--brand-red)"/>
      <rect x="0" y="4.5" width="540" height="2.5" fill="var(--brand-dark)"/>
    </svg>
  </main>
</body>
</html>
```